new letterhead/envelope/business card design for law firm

please see attached pdf of current letterhead, envelope and business card. I am also attaching my new logo that I would like to be used. basically, I am looking to refresh and simplify my letterhead/stationary and business card, keeping the following in mind:

overall, I am going for the following look:

-simple,
-modern,
-classy,
-professional

Target Market(s)

law firm clients

Industry/Entity Type

Law Firm

Contact Information for Business Card

see attachment

Font styles to use
Sans Serif

Requirements
Must have
• overall, I am going for the following look:
• -simple,
• -modern,
• -classy,
• -professional
Nice to have
• same as above
Should not have
• no serif fonts

```html
<!DOCTYPE html>
<html lang="en">
<head>
<meta charset="utf-8">
<title>Hollis Law Stationery</title>
<link href="https://fonts.googleapis.com/css2?family=Montserrat:wght@600&family=Poppins:wght@300;400&family=Roboto:wght@400;500;700&display=swap" rel="stylesheet">
<style>
  :root {
    --backdrop: #dcdcdc;
    --paper: #f7f7f7;
    --paper-edge: #efefef;
    --navy: #0d2a4d;
    --green: #1f5a3a;
    --text: #555a60;
    --muted: #6a6f75;
  }
  * { margin: 0; padding: 0; box-sizing: border-box; }
  html, body { width: 1200px; height: 877px; overflow: hidden; }
  body { background: var(--backdrop); position: relative; font-family: "Roboto", sans-serif; color: var(--text); }

  .sheet {
    position: absolute;
    background: linear-gradient(90deg, var(--paper) 0%, #fbfbfb 50%, var(--paper-edge) 100%);
    box-shadow: 0 2px 6px rgba(0,0,0,.18);
  }

  /* brand mark: plain circle with name */
  .brand { position: absolute; text-align: center; }
  .brand-dot {
    display: block; margin: 0 auto;
    border-radius: 50%;
    background: linear-gradient(180deg, var(--green), var(--navy));
    border: 2px solid #fff; box-shadow: 0 0 0 1.5px var(--navy);
  }
  .brand-name {
    display: block; font-family: "Montserrat", sans-serif; font-weight: 600;
    color: var(--navy); letter-spacing: 2px; white-space: nowrap;
  }

  /* letterhead */
  .letterhead { left: 58px; top: 64px; width: 527px; height: 742px; }
  .letterhead .brand { left: 45px; top: 46px; width: 126px; }
  .letterhead .brand-dot { width: 44px; height: 44px; }
  .letterhead .brand-name { font-size: 19px; margin-top: 10px; }
  .contact-block { position: absolute; right: 39px; top: 41px; text-align: right; font-size: 7.6px; line-height: 10px; color: var(--muted); }
  .contact-block .attorney { font-weight: 700; color: var(--navy); font-size: 8.8px; margin-bottom: 2px; letter-spacing: .2px; }
  .contact-block .gap { height: 4px; }
  .contact-line { display: flex; justify-content: flex-end; align-items: center; gap: 4px; }
  .contact-line svg { width: 7px; height: 7px; fill: var(--navy); }

  .letter { position: absolute; left: 45px; top: 207px; width: 440px; font-family: "Poppins", sans-serif; font-weight: 300; }
  .salutation { font-size: 13px; color: var(--text); font-weight: 300; margin-bottom: 23px; }
  .letter p { font-size: 7.3px; line-height: 11.4px; color: var(--text); margin-bottom: 11.5px; }
  .closing { font-size: 7.4px; margin-top: 22px; }
  .signature { position: absolute; left: 41px; top: 516px; width: 96px; height: 44px; border-radius: 6px;
    background: linear-gradient(90deg, rgba(43,90,168,.16), rgba(43,90,168,.06)); }

  /* business cards */
  .card { width: 252px; height: 144px; top: 88px; }
  .card-front { left: 606px; }
  .card-back { left: 878px; }
  .card-front .brand { left: 19px; top: 44px; width: 90px; }
  .card-front .brand-dot { width: 32px; height: 32px; }
  .card-front .brand-name { font-size: 13px; margin-top: 6px; letter-spacing: 1.4px; }
  .card-info { position: absolute; right: 19px; top: 26px; text-align: right; font-size: 5.8px; line-height: 8px; color: var(--muted); }
  .card-info .attorney { font-weight: 700; color: var(--navy); font-size: 8px; line-height: 9px; }
  .card-info .license { color: var(--green); margin-bottom: 21px; }
  .card-info .gap { height: 6px; }
  .card-info b { color: var(--navy); font-weight: 700; }
  .card-back .brand { left: 0; right: 0; top: 36px; }
  .card-back .brand-dot { width: 38px; height: 38px; }
  .card-back .brand-name { font-size: 17px; margin-top: 8px; }
  .card-web { position: absolute; left: 0; right: 0; top: 122px; text-align: center; font-size: 6px; letter-spacing: 2.6px; color: var(--muted); }

  /* envelopes */
  .envelope-back { left: 603px; top: 269px; width: 531px; height: 240px; overflow: hidden; }
  .flap { position: absolute; left: 0; top: 0; width: 531px; height: 80px; filter: drop-shadow(0 3px 3px rgba(0,0,0,.12)); }
  .envelope-back .brand { left: 0; right: 0; top: 20px; }
  .envelope-back .brand-dot { width: 34px; height: 34px; }
  .envelope-front { left: 603px; top: 562px; width: 533px; height: 242px; }
  .envelope-front .brand { left: 34px; top: 34px; width: 100px; }
  .envelope-front .brand-dot { width: 36px; height: 36px; }
  .envelope-front .brand-name { font-size: 15px; margin-top: 8px; letter-spacing: 1.6px; }
  .return-address { position: absolute; left: 24px; top: 103px; width: 124px; text-align: center; font-size: 7.4px; line-height: 10px; color: var(--navy); }
</style>
</head>
<body>

  <section class="sheet letterhead">
    <div class="brand">
      <span class="brand-dot"></span>
      <span class="brand-name">HOLLIS LAW</span>
    </div>
    <div class="contact-block">
      <div class="attorney">DANIEL R. HOLLIS, ESQ.</div>
      <div>Licensed in NC and VA</div>
      <div>Certified Specialist in Civil Litigation</div>
      <div class="gap"></div>
      <div>2240 Crescent Avenue, Suite 410</div>
      <div>Raleigh, NC 27605</div>
      <div class="gap"></div>
      <div class="contact-line">919.555.0142
        <svg viewBox="0 0 10 10"><path d="M2 0.5 L3.8 2.6 L2.9 3.9 Q4 6 6.1 7.1 L7.4 6.2 L9.5 8 L8.4 9.5 Q4.5 9.6 2 6.6 Q0 4 0.5 1.6 Z"/></svg></div>
      <div class="contact-line">919.555.0187
        <svg viewBox="0 0 10 10"><rect x="2.5" y="0.5" width="5" height="3"/><rect x="0.5" y="3.5" width="9" height="4" rx="1"/><rect x="2.5" y="6.5" width="5" height="3"/></svg></div>
      <div class="contact-line">www.hollislawpa.com
        <svg viewBox="0 0 10 10"><circle cx="5" cy="5" r="4.5"/><path d="M3 3 Q5 2 6 4 Q4 5 5 7" stroke="#fff" stroke-width="1" fill="none"/></svg></div>
    </div>

    <div class="letter">
      <div class="salutation">Dear Mr. Carter,</div>
      <p>Lorem ipsum dolor sit amet, consectetur adipiscing elit. Donec orci purus, luctus vitae dignissim eu, iaculis sed purus. Vivamus faucibus, ipsum nec aliquet viverra, leo mauris condimentum ligula, sit amet sagittis enim ligula quis arcu. Nam egestas tortor id nisi porttitor mattis. In tortor ante, ultricies in suscipit a, tempus non massa. Vivamus et auctor mi. Fusce vel massa nulla. Phasellus nec eros mauris, et scelerisque orci.</p>
      <p>Donec malesuada orci vitae nulla accumsan porta a id massa. Quisque accumsan iaculis magna sit amet fringilla. Maecenas consequat, magna eget tincidunt semper, odio nibh rutrum mi, id feugiat ante nisi eu risus. Vestibulum nunc orci, rhoncus a placerat in, ultricies in mi. Cras mattis varius eros, vel fringilla nisi suscipit eget. Quisque scelerisque sagittis nulla at porttitor.</p>
      <p>Sed id augue vitae urna euismod commodo aliquet a quam. Pellentesque arcu velit, cursus et malesuada ut, consequat et diam. Nullam erat sem, rhoncus id ullamcorper vitae, rhoncus et arcu. In ultricies ultricies nulla, ut rutrum nisi iaculis at. Donec eu magna a metus ornare faucibus. Fusce aliquet faucibus ultricies. Morbi semper, est id tincidunt gravida, sem arcu adipiscing lacus, ac bibendum nulla leo eu purus. Quisque nec diam sed risus consectetur a ccumsan quis quis nibh. Vestibulum id purus lorem.</p>
      <p>It is a long established fact that a reader will be distracted by the readable content of a page when looking at its layout. The point of using Lorem Ipsum is that it has a more-or-less normal distribution of letters, as opposed to using 'Content here, content here', making it look like readable English. Many desktop publishing packages</p>
      <div class="closing">Sincerely,</div>
    </div>
    <div class="signature" role="img" aria-label="Handwritten signature of the sender in blue ink"></div>
  </section>

  <section class="sheet card card-front">
    <div class="brand">
      <span class="brand-dot"></span>
      <span class="brand-name">HOLLIS LAW</span>
    </div>
    <div class="card-info">
      <div class="attorney">DANIEL R. HOLLIS, ESQ.</div>
      <div class="license">Licensed in NC and VA.</div>
      <div>2240 Crescent Avenue, Suite 410</div>
      <div>Raleigh, NC 27605</div>
      <div class="gap"></div>
      <div><b>Tel:</b> 919.555.0142</div>
      <div><b>Cell:</b> 919.555.0163</div>
      <div><b>Fax:</b> 919.555.0187</div>
      <div>www.hollislawpa.com</div>
      <div>dan@hollislawpa.com</div>
    </div>
  </section>

  <section class="sheet card card-back">
    <div class="brand">
      <span class="brand-dot"></span>
      <span class="brand-name">HOLLIS LAW</span>
    </div>
    <div class="card-web">www.hollislawpa.com</div>
  </section>

  <section class="sheet envelope-back">
    <svg class="flap" viewBox="0 0 531 80" aria-hidden="true">
      <path d="M0 0 H531 L524 22 Q512 75 470 75 H62 Q18 75 8 22 Z" fill="#fafafa"/>
    </svg>
    <div class="brand"><span class="brand-dot"></span></div>
  </section>

  <section class="sheet envelope-front">
    <div class="brand">
      <span class="brand-dot"></span>
      <span class="brand-name">HOLLIS LAW</span>
    </div>
    <div class="return-address">2240 Crescent Avenue,<br>Suite 410, Raleigh, NC 27605</div>
  </section>

</body>
</html>
```